Corporate consulting business needs a business card

I want a professional business card.... surprise me

Updates

Reason: i dont think 2 days is enough

Target Market(s)

Corprorate and Not for Profit firms and organisations

Industry/Entity Type

Consulting

Contact Information for Business Card

Logo
Corporate Consulting Services
Clear Advice, Sound Plans, Lasting Results
Tovan Presfield
Director
0427 31 94 62 (Larger)
tovan@tp-advisory.com.au
www.tp-advisory.com.au
include little icons beside the contact info:

- Envelope = email
- Phone = phone
- Globe = website

Font styles to use
Serif
Sans Serif

Requirements
Must have
• Professional and clean
Nice to have
• you tell me

```html
<!DOCTYPE html>
<html lang="en">
<head>
<meta charset="utf-8">
<title>TP Advisory Services – Business Card</title>
<link href="https://fonts.googleapis.com/css2?family=Cormorant+Garamond:wght@600&family=Fira+Sans:ital,wght@0,400;0,600;1,400&display=swap" rel="stylesheet">
<style>
  :root {
    --bg: #d9d9d9;
    --card: #ffffff;
    --brown: #4a1f0c;
    --brown-dark: #2e1206;
    --brown-accent: #6b2f12;
    --ink: #141414;
    --muted: #2b2b2b;
    --faint: #f1e7e1;
    --on-brown: #ffffff;
  }
  * { box-sizing: border-box; margin: 0; padding: 0; }
  html, body { width: 1200px; height: 960px; overflow: hidden; }
  body {
    background: var(--bg);
    font-family: "Fira Sans", Arial, sans-serif;
    position: relative;
  }
  .card {
    position: absolute;
    left: 250px;
    width: 700px;
    height: 400px;
    background: var(--card);
    box-shadow: 0 8px 24px rgba(0,0,0,.18);
    overflow: hidden;
  }
  .card--front { top: 60px; }
  .card--back { top: 500px; display: flex; }

  /* Front */
  .front-decor {
    position: absolute;
    right: -110px;
    bottom: -170px;
    width: 300px;
    height: 300px;
    border: 6px solid var(--faint);
    border-radius: 50%;
  }
  .front-mark {
    position: absolute;
    left: 0; right: 0; top: 110px;
    display: flex;
    align-items: center;
    justify-content: center;
    gap: 22px;
  }
  .mark-circle {
    width: 78px; height: 78px;
    border: 5px solid var(--brown);
    border-radius: 50%;
    flex: none;
  }
  .front-name {
    font-family: "Cormorant Garamond", Georgia, serif;
    font-weight: 600;
    font-size: 52px;
    color: var(--brown);
    letter-spacing: 1px;
  }
  .front-descriptor {
    position: absolute;
    left: 0; right: 0; top: 236px;
    text-align: center;
    font-family: "Cormorant Garamond", Georgia, serif;
    font-weight: 600;
    font-size: 34px;
    letter-spacing: 3px;
    color: var(--ink);
    text-transform: uppercase;
  }

  /* Back */
  .band {
    width: 270px;
    height: 100%;
    background: linear-gradient(160deg, var(--brown) 0%, var(--brown-dark) 100%);
    color: var(--on-brown);
    padding: 70px 24px 0;
    display: flex;
    flex-direction: column;
    align-items: center;
    text-align: center;
  }
  .band-mark { display: flex; align-items: center; gap: 12px; }
  .band-circle {
    width: 34px; height: 34px;
    border: 3px solid var(--on-brown);
    border-radius: 50%;
  }
  .band-name {
    font-family: "Cormorant Garamond", Georgia, serif;
    font-weight: 600;
    font-size: 32px;
  }
  .band-service {
    margin-top: 26px;
    font-weight: 600;
    font-size: 15px;
    line-height: 1.45;
    letter-spacing: .5px;
    text-transform: uppercase;
  }
  .band-tagline {
    margin-top: 26px;
    font-style: italic;
    font-size: 15px;
    line-height: 1.5;
  }
  .details {
    flex: 1;
    padding: 78px 48px 0 40px;
    text-align: right;
  }
  .person-name { font-weight: 600; font-size: 28px; color: var(--ink); }
  .person-role { font-size: 18px; color: var(--brown-accent); margin-top: 2px; }
  .contact { list-style: none; margin-top: 64px; }
  .contact li {
    display: flex;
    justify-content: flex-end;
    align-items: center;
    gap: 12px;
    font-size: 17px;
    color: var(--muted);
    margin-top: 8px;
  }
  .contact li.contact-phone { font-size: 22px; font-weight: 600; color: var(--ink); }
  .contact svg { width: 18px; height: 18px; flex: none; }
</style>
</head>
<body>
  <section class="card card--front" aria-label="Card front">
    <div class="front-decor" aria-hidden="true"></div>
    <div class="front-mark">
      <span class="mark-circle" aria-hidden="true"></span>
      <span class="front-name">TP Advisory</span>
    </div>
    <p class="front-descriptor">Consulting Services</p>
  </section>

  <section class="card card--back" aria-label="Card back">
    <div class="band">
      <div class="band-mark">
        <span class="band-circle" aria-hidden="true"></span>
        <span class="band-name">TP Advisory</span>
      </div>
      <p class="band-service">Corporate<br>Consulting Services</p>
      <p class="band-tagline">Clear Advice, Sound Plans,<br>Lasting Results</p>
    </div>
    <div class="details">
      <h1 class="person-name">Tovan Presfield</h1>
      <p class="person-role">Director</p>
      <ul class="contact">
        <li class="contact-phone">0427 31 94 62
          <svg viewBox="0 0 24 24" aria-hidden="true"><path fill="#6b2f12" d="M6.6 10.8a15.5 15.5 0 0 0 6.6 6.6l2.2-2.2a1 1 0 0 1 1-.25 11.4 11.4 0 0 0 3.6.57 1 1 0 0 1 1 1V20a1 1 0 0 1-1 1A17 17 0 0 1 3 4a1 1 0 0 1 1-1h3.5a1 1 0 0 1 1 1c0 1.250.2 2.450.57 3.57a1 1 0 0 1-.25 1z"/></svg>
        </li>
        <li>tovan@tp-advisory.com.au
          <svg viewBox="0 0 24 24" aria-hidden="true"><rect x="3" y="5" width="18" height="14" rx="1.5" fill="none" stroke="#6b2f12" stroke-width="2"/><path d="M3.5 6l8.5 7 8.5-7" fill="none" stroke="#6b2f12" stroke-width="2"/></svg>
        </li>
        <li>www.tp-advisory.com.au
          <svg viewBox="0 0 24 24" aria-hidden="true"><circle cx="12" cy="12" r="9" fill="none" stroke="#6b2f12" stroke-width="2"/><ellipse cx="12" cy="12" rx="4" ry="9" fill="none" stroke="#6b2f12" stroke-width="1.6"/><path d="M3 12h18" stroke="#6b2f12" stroke-width="1.6"/></svg>
        </li>
      </ul>
    </div>
  </section>
</body>
</html>
```